Website for The Velvet Pathfinder

We need an impressive e-commerce website for our newly launched business "The Velvet Pathfinder".
The Velvet Pathfinder searches store-front and online retailers for diamond engagement rings according to the client's specified requirements. We want to save people time by doing the shopping around for them.
We can relate to, and we love, www.corvaline.com
Like corvaline.com, we want to offer website visitors a quick run-down on how the process works, then offer them to elect a service package and pay for that package on the spot.
Content pages:
HOME
HOW IT WORKS
DIAMOND GALLERY
ABOUT
FAQs
CONTACT
Inclusions: Our logo and Facebook and Instagram buttons
We want to be able to easily edit this website, We want it to display well on iPhone and android, We want it to be clean and striking.
Like our logo, we want our website to embody elegant masculinity.
Target Market(s)
Men in market for diamond ring purchase $5k - $50k
Industry/Entity Type
Business
Number of Pages Required
5+ page
Font styles to use
Look and feel

```html
<!DOCTYPE html>
<html lang="en">
<head>
<meta charset="utf-8">
<title>How It Works – The Velvet Pathfinder</title>
<link rel="stylesheet" href="https://fonts.googleapis.com/css2?family=Bebas+Neue&family=Lato:wght@400;700&family=Montserrat:wght@400&display=swap">
<style>
  :root {
    --ink: #555555;
    --ink-dark: #5a5a5a;
    --rule: #666666;
    --hero-top: #8c8c8c;
    --hero-bottom: #666666;
    --crumb-bg: #b3b3b3;
    --paper: #ffffff;
  }
  * { margin: 0; padding: 0; box-sizing: border-box; }
  html, body {
    width: 1200px;
    height: 3699px;
    overflow: hidden;
    background: var(--paper);
  }
  .page {
    position: relative;
    width: 1200px;
    height: 3699px;
    font-family: "Lato", Arial, sans-serif;
    color: var(--ink);
  }
  .top-rule {
    position: absolute;
    left: 0; top: 176px;
    width: 1200px; height: 10px;
    background: var(--rule);
  }
  .site-header {
    position: absolute;
    left: 0; top: 186px;
    width: 1200px; height: 675px;
  }
  .header-button {
    position: absolute;
    top: 265px;
    width: 134px; height: 134px;
    border-radius: 19px;
    background: var(--ink-dark);
    display: flex;
    align-items: center;
    justify-content: center;
  }
  .header-button--menu { left: 138px; }
  .header-button--account { left: 928px; }
  .brand-name {
    position: absolute;
    left: 300px; top: 290px;
    width: 600px;
    text-align: center;
    font-family: "Lato", Arial, sans-serif;
    font-weight: 400;
    font-size: 62px;
    line-height: 1.15;
    letter-spacing: 4px;
    text-transform: uppercase;
    color: var(--rule);
  }
  .hero {
    position: absolute;
    left: 0; top: 861px;
    width: 1200px; height: 368px;
    background: linear-gradient(180deg, var(--hero-top), var(--hero-bottom));
    display: flex;
    align-items: center;
    justify-content: center;
  }
  .hero-title {
    font-family: "Bebas Neue", Impact, sans-serif;
    font-weight: 400;
    font-size: 164px;
    line-height: 1;
    color: var(--paper);
    padding-top: 10px;
  }
  .breadcrumb {
    position: absolute;
    left: 0; top: 1229px;
    width: 1200px; height: 134px;
    background: var(--crumb-bg);
    padding-left: 150px;
    display: flex;
    align-items: center;
    font-weight: 700;
    font-size: 48px;
    color: var(--ink);
  }
  .step {
    position: absolute;
    left: 0;
    width: 1200px;
    text-align: center;
  }
  .step--one { top: 1530px; }
  .step--two { top: 2298px; }
  .step--three { top: 3066px; }
  .step-icon {
    display: block;
    margin: 0 auto;
    width: 256px; height: 256px;
  }
  .step-number {
    font-family: "Montserrat", Arial, sans-serif;
    font-weight: 400;
    font-size: 118px;
    line-height: 1;
    margin-top: -6px;
    color: var(--ink);
  }
  .step-text {
    font-size: 48px;
    line-height: 77px;
    margin-top: 0;
    color: var(--ink);
  }
</style>
</head>
<body>
<div class="page">
  <div class="top-rule"></div>

  <header class="site-header">
    <div class="header-button header-button--menu" aria-label="Menu">
      <svg width="44" height="40" viewBox="0 0 44 40">
        <rect x="0" y="2" width="44" height="7" rx="2" fill="#fff"/>
        <rect x="0" y="16.5" width="44" height="7" rx="2" fill="#fff"/>
        <rect x="0" y="31" width="44" height="7" rx="2" fill="#fff"/>
      </svg>
    </div>
    <div class="brand-name">The Velvet<br>Pathfinder</div>
    <div class="header-button header-button--account" aria-label="Account">
      <svg width="40" height="44" viewBox="0 0 40 44">
        <circle cx="20" cy="11" r="10" fill="#fff"/>
        <path d="M2 44 C2 30 10 24 20 24 C30 24 38 30 38 44 Z" fill="#fff"/>
      </svg>
    </div>
  </header>

  <section class="hero">
    <h1 class="hero-title">How It Works</h1>
  </section>

  <nav class="breadcrumb">Home &gt; How It Works</nav>

  <section class="step step--one">
    <svg class="step-icon" viewBox="0 0 256 256">
      <circle cx="128" cy="128" r="124" fill="none" stroke="#555" stroke-width="6"/>
      <path d="M112 96 H92 a8 8 0 0 0 -8 8 V164 a8 8 0 0 0 8 8 H152 a8 8 0 0 0 8 -8 V144" fill="none" stroke="#555" stroke-width="8" stroke-linecap="round"/>
      <path d="M118 148 L122 128 L158 92 L174 108 L138 144 Z" fill="#555"/>
      <path d="M162 88 L170 80 L186 96 L178 104 Z" fill="#555"/>
    </svg>
    <div class="step-number">1</div>
    <p class="step-text">Lorem ipsum dolor sit amet, consectetur<br>adipiscing elit.</p>
  </section>

  <section class="step step--two">
    <svg class="step-icon" viewBox="0 0 256 256">
      <circle cx="128" cy="128" r="124" fill="none" stroke="#555" stroke-width="6"/>
      <path d="M80 104 a8 8 0 0 1 8 -8 H104 L112 84 H144 L152 96 H168 a8 8 0 0 1 8 8 V164 a8 8 0 0 1 -8 8 H88 a8 8 0 0 1 -8 -8 Z" fill="#555"/>
      <circle cx="128" cy="134" r="22" fill="#fff"/>
      <circle cx="128" cy="134" r="13" fill="#555"/>
    </svg>
    <div class="step-number">2</div>
    <p class="step-text">Lorem ipsum dolor sit amet, consectetur<br>adipiscing elit.</p>
  </section>

  <section class="step step--three">
    <svg class="step-icon" viewBox="0 0 256 256">
      <circle cx="128" cy="128" r="124" fill="none" stroke="#555" stroke-width="6"/>
      <rect x="82" y="90" width="92" height="76" rx="4" fill="none" stroke="#555" stroke-width="8"/>
      <circle cx="104" cy="112" r="9" fill="#555"/>
      <path d="M92 156 L114 134 L126 146 L146 122 L164 142 V156 Z" fill="#555"/>
    </svg>
    <div class="step-number">3</div>
    <p class="step-text">Lorem ipsum dolor sit amet, consectetur<br>adipiscing elit.</p>
  </section>
</div>
</body>
</html>
```